Stylish Homeware business needs a Logo and Business Card design

We need a logo and business card for a new company based in Hong Kong called "Nest Lumora". We do marketing and distributing international stylish Homeware brands in Asia. Products we handle included clocks, picture frame, small kitchen wares, LED lightenings, stationary and etc. We planned to also create our own brands next step. We could like to see designs that use pastel colors. The final design shoudl be simple and stylish.
Target Market(s)
Asia, Mainly Japan, China and Korea
Industry/Entity Type
Business
Contact Information for Business Card
We could like to see designs that use pastel colors. The final design shoudl be simple and stylish. We attach some log design we like on the bottom of the page.
Font styles to use
Look and feel
Each slider illustrates characteristics of the customer's brand and the style your logo design should communicate.

```html
<!DOCTYPE html>
<html lang="en">
<head>
<meta charset="utf-8">
<title>Nest Lumora — Business Cards</title>
<link rel="stylesheet" href="https://fonts.googleapis.com/css2?family=Montserrat:wght@300;400;600;700&family=Lora:wght@500&display=swap">
<style>
  :root {
    --teal: #2a8f95;
    --teal-deep: #23797e;
    --paper: #f4f4f2;
    --ink: #6b6b6b;
    --ink-strong: #555555;
    --backdrop: #e9e7e3;
  }
  * { box-sizing: border-box; margin: 0; padding: 0; }
  html, body {
    width: 1200px;
    height: 775px;
    overflow: hidden;
    background: var(--backdrop);
  }
  .stage {
    position: relative;
    width: 1200px;
    height: 775px;
    display: flex;
    justify-content: center;
    align-items: center;
    gap: 70px;
  }
  .card {
    width: 300px;
    height: 525px;
    position: relative;
    box-shadow: 0 6px 18px rgba(0, 0, 0, 0.12);
  }
  .card-front {
    background: var(--teal);
    display: flex;
    justify-content: center;
    align-items: center;
  }
  .card-back {
    background: var(--paper);
  }
  .brand-name {
    font-family: "Montserrat", sans-serif;
    font-weight: 600;
    text-transform: uppercase;
    letter-spacing: 0.32em;
    white-space: nowrap;
  }
  .card-front .brand-name {
    color: #ffffff;
    font-size: 17px;
    margin-top: -30px;
  }
  .card-back .brand-name {
    color: var(--teal);
    font-size: 14px;
    position: absolute;
    top: 110px;
    left: 0;
    right: 0;
    text-align: center;
  }
  .contact-block {
    position: absolute;
    left: 60px;
    top: 250px;
    font-family: "Montserrat", sans-serif;
    color: var(--ink);
  }
  .person-name {
    font-size: 19px;
    font-weight: 300;
    color: var(--ink);
  }
  .person-name strong {
    font-weight: 700;
    color: var(--ink-strong);
  }
  .job-title {
    font-family: "Lora", serif;
    font-weight: 500;
    color: var(--teal);
    font-size: 14px;
    margin-top: 2px;
  }
  .contact-list {
    list-style: none;
    margin-top: 20px;
    font-size: 12.5px;
  }
  .contact-list li {
    display: flex;
    align-items: center;
    gap: 12px;
    margin-bottom: 7px;
  }
  .contact-list svg {
    width: 12px;
    height: 12px;
    flex: none;
    fill: var(--teal);
  }
</style>
</head>
<body>
<main class="stage">
  <section class="card card-front" aria-label="Card front">
    <p class="brand-name">Nest Lumora</p>
  </section>

  <section class="card card-back" aria-label="Card back">
    <p class="brand-name">Nest Lumora</p>
    <div class="contact-block">
      <p class="person-name">Your <strong>Name</strong></p>
      <p class="job-title">Job Title</p>
      <ul class="contact-list">
        <li>
          <svg viewBox="0 0 12 12" aria-hidden="true"><path d="M6 0.5a4 4 0 0 0-4 4c0 3 4 7 4 7s4-4 4-7a4 4 0 0 0-4-4zm0 5.6a1.6 1.6 0 1 1 0-3.2 1.6 1.6 0 0 1 0 3.2z"/></svg>
          <span>your address</span>
        </li>
        <li>
          <svg viewBox="0 0 12 12" aria-hidden="true"><path d="M1 4.2c0-1.2 2.3-2.2 5-2.2s5 1 5 2.2v0.9H8.4V4.1c-0.7-0.3-1.5-0.4-2.4-0.4s-1.7 0.1-2.4 0.4v1H1z"/><rect x="2" y="6" width="8" height="4.5" rx="0.8"/></svg>
          <span>000 000 0000</span>
        </li>
        <li>
          <svg viewBox="0 0 12 12" aria-hidden="true"><path d="M6 0.5a5.5 5.5 0 1 0 0 11 5.5 5.5 0 0 0 0-11zm0 1c0.7 0 1.5 1.5 1.7 3.8H4.3C4.5 3 5.3 1.5 6 1.5zM1.6 6.7h1.7c0.1 1.3 0.4 2.4 0.8 3.2a4.5 4.5 0 0 1-2.5-3.2zm0-1.4a4.5 4.5 0 0 1 2.5-3.2c-0.4 0.8-0.7 1.9-0.8 3.2zM6 10.5c-0.7 0-1.5-1.5-1.7-3.8h3.4c-0.2 2.3-1 3.8-1.7 3.8zm1.9-0.6c0.4-0.8 0.7-1.9 0.8-3.2h1.7a4.5 4.5 0 0 1-2.5 3.2zm0.8-4.6c-0.1-1.3-0.4-2.4-0.8-3.2a4.5 4.5 0 0 1 2.5 3.2z"/></svg>
          <span>youremail@nestlumora.com</span>
        </li>
      </ul>
    </div>
  </section>
</main>
</body>
</html>
```